Business Cards, Letterheads, Envelopes

A company's new identity to be reflected on its stationery items

Target Market(s)

Large Corporate Companies & Enterprises

Font styles to use
Sans Serif

Colors
0555a3
3176b5
85abd2
85cae6
33a6d7
0293ce

```html
<!DOCTYPE html>
<html lang="en">
<head>
<meta charset="utf-8">
<title>Nexalink Group – Stationery Set</title>
<link href="https://fonts.googleapis.com/css2?family=Source+Sans+3:wght@400;600&display=swap" rel="stylesheet">
<style>
  :root {
    --brand-blue: #3176b5;
    --ink: #222;
    --dark: #2b2b2b;
    --paper: #f4f4f4;
    --backdrop: #e2e2e4;
    --rule: #9a9a9a;
    --on-dark: #e6e6e6;
  }
  * { margin: 0; padding: 0; box-sizing: border-box; }
  html, body { width: 1200px; height: 926px; overflow: hidden; }
  body {
    background: var(--backdrop);
    font-family: "Source Sans 3", sans-serif;
    color: var(--ink);
    position: relative;
  }
  .sheet { position: absolute; background: var(--paper); overflow: hidden; }
  .footer-band { position: absolute; left: 0; bottom: 0; width: 100%; }
  .footer-url { position: absolute; right: 0; color: #fff; text-align: center; white-space: nowrap; }
  .wordmark { position: absolute; display: flex; align-items: center; gap: 6px; }
  .wordmark__dot { border-radius: 50%; background: var(--brand-blue); flex: none; }
  .wordmark__name { color: var(--ink); font-weight: 600; line-height: 1; white-space: nowrap; }
  .contact { position: absolute; line-height: 1.3; font-style: normal; white-space: nowrap; }
  .contact .icon { display: inline-block; vertical-align: -1px; margin-right: 2px; }

  /* Letterhead */
  .letterhead { left: 103px; top: 144px; width: 447px; height: 631px; }
  .letterhead .wordmark { left: 29px; top: 31px; }
  .letterhead .wordmark__dot { width: 20px; height: 20px; }
  .letterhead .wordmark__name { font-size: 15px; }
  .letterhead .contact {
    left: 302px; top: 23px; padding-left: 8px; border-left: 1px solid var(--rule);
    font-size: 6.8px;
  }
  .letterhead .contact p.gap { margin-top: 3px; }
  .letterhead .footer-url { bottom: 3px; width: 125px; font-size: 7.5px; }

  /* Business cards */
  .card { top: 163px; width: 190px; height: 108px; }
  .card-front { left: 581px; }
  .card-front .wordmark { left: 13px; top: 15px; gap: 4px; }
  .card-front .wordmark__dot { width: 12px; height: 12px; }
  .card-front .wordmark__name { font-size: 9px; }
  .card-holder { position: absolute; right: 11px; top: 48px; text-align: right; line-height: 1.2; }
  .card-holder__name { color: var(--brand-blue); font-size: 6.6px; font-weight: 600; }
  .card-holder__role { font-size: 4.8px; }
  .card-front .contact { left: 13px; top: 67px; font-size: 4.6px; }
  .card-front .contact p.gap { margin-top: 2px; }
  .card-front .footer-url { bottom: 2px; width: 72px; font-size: 4.8px; }

  .card-back { left: 810px; background: var(--dark); }
  .card-back__texture {
    position: absolute; inset: 0;
    background: radial-gradient(circle at 40% 40%, #353535, #262626 75%);
  }
  .card-back .wordmark { left: 0; right: 0; top: 42px; justify-content: center; }
  .card-back .wordmark__dot { width: 16px; height: 16px; }
  .card-back .wordmark__name { font-size: 12px; color: var(--on-dark); }
  .card-back__url {
    position: absolute; left: 0; right: 0; top: 91px; text-align: center;
    font-size: 5.4px; letter-spacing: .12em; color: #b8b8b8;
  }
  .card-back__url span { color: var(--brand-blue); }

  /* Envelopes */
  .envelope { left: 582px; width: 513px; height: 223px; }
  .envelope-front { top: 309px; }
  .envelope-front .wordmark { left: 20px; top: 22px; gap: 6px; }
  .envelope-front .wordmark__dot { width: 20px; height: 20px; }
  .envelope-front .wordmark__name { font-size: 14px; }
  .envelope-front .contact { left: 20px; top: 59px; font-size: 6.4px; }
  .envelope-front .footer-url { bottom: 4px; width: 118px; font-size: 6.6px; }

  .envelope-back { top: 553px; }
  .envelope-flap { position: absolute; left: 0; top: 0; }
  .envelope-back .wordmark { left: 0; right: 0; top: 30px; justify-content: center; }
  .envelope-back .wordmark__dot { width: 16px; height: 16px; }
  .envelope-back .wordmark__name { font-size: 12px; color: var(--on-dark); }
</style>
</head>
<body>

<section class="sheet letterhead" aria-label="Letterhead">
  <div class="wordmark">
    <span class="wordmark__dot"></span>
    <span class="wordmark__name">Nexalink Group</span>
  </div>
  <address class="contact">
    <p>412B, Lakeview Business Park, Ramnagar</p>
    <p>Pune, Maharashtra 411045</p>
    <p class="gap"><svg class="icon" width="6" height="6" viewBox="0 0 10 10"><path d="M2 0.5 L4 2.5 L3 4 Q4.5 6 6 7 L7.5 6 L9.5 8 L8 9.5 Q3 9 0.5 2 Z" fill="var(--brand-blue)"/></svg>+91 20 555 0182</p>
    <p><svg class="icon" width="6" height="5" viewBox="0 0 10 8"><rect x=".5" y=".5" width="9" height="7" fill="none" stroke="var(--brand-blue)"/><path d="M.5 .5 L5 4.5 L9.5 .5" fill="none" stroke="var(--brand-blue)"/></svg>info@nexalinktech.com</p>
  </address>
  <svg class="footer-band" width="447" height="18" viewBox="0 0 447 18">
    <rect x="0" y="3" width="447" height="6" fill="var(--dark)"/>
    <rect x="0" y="9" width="447" height="9" fill="var(--brand-blue)"/>
    <polygon points="322,0 447,0 447,18 310,18 315,9" fill="var(--brand-blue)"/>
  </svg>
  <span class="footer-url">www.nexalinktech.com</span>
</section>

<section class="sheet card card-front" aria-label="Business card front">
  <div class="wordmark">
    <span class="wordmark__dot"></span>
    <span class="wordmark__name">Nexalink Group</span>
  </div>
  <div class="card-holder">
    <p class="card-holder__name">Daniel Mercer</p>
    <p class="card-holder__role">Founder</p>
  </div>
  <address class="contact">
    <p>412B, Lakeview Business Park, Ramnagar</p>
    <p>Pune, Maharashtra 411045</p>
    <p class="gap"><svg class="icon" width="4" height="4" viewBox="0 0 10 10"><path d="M2 0.5 L4 2.5 L3 4 Q4.5 6 6 7 L7.5 6 L9.5 8 L8 9.5 Q3 9 0.5 2 Z" fill="var(--brand-blue)"/></svg>+91 20 555 0182</p>
    <p><svg class="icon" width="4" height="3.5" viewBox="0 0 10 8"><rect x=".5" y=".5" width="9" height="7" fill="none" stroke="var(--brand-blue)"/><path d="M.5 .5 L5 4.5 L9.5 .5" fill="none" stroke="var(--brand-blue)"/></svg>daniel@nexalinktech.com</p>
  </address>
  <svg class="footer-band" width="190" height="10" viewBox="0 0 190 10">
    <rect x="0" y="2" width="190" height="3" fill="var(--dark)"/>
    <rect x="0" y="5" width="190" height="5" fill="var(--brand-blue)"/>
    <polygon points="118,0 190,0 190,10 112,10 115,5" fill="var(--brand-blue)"/>
  </svg>
  <span class="footer-url">www.nexalinktech.com</span>
</section>

<section class="sheet card card-back" aria-label="Business card back">
  <div class="card-back__texture" role="img" aria-label="Subtle dark connected-dots texture"></div>
  <div class="wordmark">
    <span class="wordmark__dot"></span>
    <span class="wordmark__name">Nexalink Group</span>
  </div>
  <p class="card-back__url">www.<span>nexalink</span>tech.com</p>
</section>

<section class="sheet envelope envelope-front" aria-label="Envelope front">
  <div class="wordmark">
    <span class="wordmark__dot"></span>
    <span class="wordmark__name">Nexalink Group</span>
  </div>
  <address class="contact">
    <p>412B, Lakeview Business Park, Ramnagar</p>
    <p>Pune, Maharashtra 411045</p>
  </address>
  <svg class="footer-band" width="513" height="16" viewBox="0 0 513 16">
    <rect x="0" y="1" width="513" height="6" fill="var(--dark)"/>
    <rect x="0" y="7" width="513" height="9" fill="var(--brand-blue)"/>
    <polygon points="393,0 513,0 513,16 382,16 387,7" fill="var(--brand-blue)"/>
  </svg>
  <span class="footer-url">www.nexalinktech.com</span>
</section>

<section class="sheet envelope envelope-back" aria-label="Envelope back">
  <svg class="envelope-flap" width="513" height="75" viewBox="0 0 513 75">
    <path d="M0 0 H513 L509 62 Q508 74 496 74 H17 Q5 74 4 62 Z" fill="var(--dark)"/>
  </svg>
  <div class="wordmark">
    <span class="wordmark__dot"></span>
    <span class="wordmark__name">Nexalink Group</span>
  </div>
</section>

</body>
</html>
```